Business Card Design

Please use the Logo for colors and styles, and create a business card using the following info:

Matthias Lorbeer
Web Developer

Lorbeer Systems
+41 76 418 57 90
matthias@lorbeer-systems.ch
www.lorbeer-systems.ch

Download the logo at http://lorbeer-systems.ch/tl_files/lorbeer_systems.zip

Thanks for your works!

```html
<!DOCTYPE html>
<html lang="en">
<head>
<meta charset="utf-8">
<title>Lorbeer Systems – Business Card</title>
<link rel="stylesheet" href="https://fonts.googleapis.com/css2?family=Abril+Fatface&family=Cinzel:wght@700;900&family=Playfair+Display:wght@700;900&display=swap">
<style>
  :root {
    --paper: #ffffff;
    --brand-blue: #1f6fae;
    --swoosh-light: #3c8fd0;
    --swoosh-mid: #1a68b0;
    --swoosh-deep: #0b2d57;
    --swoosh-night: #020a18;
    --steel-top: #8fb4d9;
    --steel-mid: #4d7fb4;
    --steel-low: #2b5586;
    --ink: #0a0a0a;
    --title-blue: #1d4f86;
  }
  html, body {
    margin: 0;
    padding: 0;
    overflow: hidden;
    background: var(--paper);
  }
  .card {
    position: relative;
    width: 1200px;
    height: 700px;
    overflow: hidden;
    background: var(--paper);
  }
  .card__backdrop {
    position: absolute;
    inset: 0;
    width: 1200px;
    height: 700px;
  }
  .brand {
    position: absolute;
    left: 50px;
    top: 120px;
    margin: 0;
    font-family: "Playfair Display", serif;
    font-weight: 900;
    font-size: 92px;
    letter-spacing: 4px;
    color: var(--brand-blue);
    display: flex;
    align-items: center;
    gap: 22px;
  }
  .brand__dot {
    width: 34px;
    height: 34px;
    border-radius: 50%;
    background: var(--brand-blue);
  }
  .identity {
    position: absolute;
    left: 0;
    width: 1232px;
    top: 262px;
    text-align: center;
  }
  .identity__name {
    margin: 0;
    font-family: "Abril Fatface", serif;
    font-size: 104px;
    line-height: 1;
    letter-spacing: 2px;
    background: linear-gradient(180deg, var(--steel-top) 0%, var(--steel-mid) 45%, var(--steel-low) 100%);
    -webkit-background-clip: text;
    background-clip: text;
    color: transparent;
    -webkit-text-stroke: 1.5px #1a1a1a;
  }
  .identity__role {
    margin: 6px 0 0;
    font-family: "Cinzel", serif;
    font-weight: 900;
    font-size: 44px;
    letter-spacing: 3px;
    color: var(--title-blue);
    -webkit-text-stroke: 1px #111;
  }
  .contact {
    position: absolute;
    left: 0;
    width: 1204px;
    top: 446px;
    text-align: center;
    font-family: "Playfair Display", serif;
    font-weight: 900;
    color: var(--ink);
    text-shadow: 0 0 6px rgba(255,255,255,0.9), 0 0 2px rgba(255,255,255,0.9);
  }
  .contact p { margin: 0; line-height: 1.18; }
  .contact__company { font-size: 36px; }
  .contact__phone { font-size: 50px; letter-spacing: 2px; }
  .contact__email { font-size: 37px; }
  .contact__web { font-size: 37px; }
</style>
</head>
<body>
<main class="card">
  <svg class="card__backdrop" viewBox="0 0 1200 700" aria-hidden="true">
    <defs>
      <linearGradient id="swoosh-fill" x1="0.3" y1="0.3" x2="1" y2="1">
        <stop offset="0" stop-color="var(--swoosh-light)"/>
        <stop offset="0.35" stop-color="var(--swoosh-mid)"/>
        <stop offset="0.7" stop-color="var(--swoosh-deep)"/>
        <stop offset="1" stop-color="var(--swoosh-night)"/>
      </linearGradient>
      <filter id="soft-edge" x="-10%" y="-10%" width="120%" height="120%">
        <feGaussianBlur stdDeviation="14"/>
      </filter>
      <filter id="soft-shade" x="-20%" y="-20%" width="140%" height="140%">
        <feGaussianBlur stdDeviation="40"/>
      </filter>
    </defs>
    <rect class="backdrop__paper" width="1200" height="700" fill="var(--paper)"/>
    <path class="backdrop__swoosh" filter="url(#soft-edge)" fill="url(#swoosh-fill)"
          d="M1090,-40 C1000,120 1060,260 900,420 C760,560 420,560 -40,530 L-40,760 L1260,760 L1260,-40 Z"/>
    <path class="backdrop__shade" filter="url(#soft-shade)" fill="var(--swoosh-night)" opacity="0.85"
          d="M1260,300 C1150,480 900,640 600,720 L1260,760 Z"/>
    <path class="backdrop__shade" filter="url(#soft-shade)" fill="var(--swoosh-night)" opacity="0.6"
          d="M-40,640 C300,620 600,660 800,760 L-40,760 Z"/>
  </svg>

  <h2 class="brand"><span class="brand__name">LORBEER SYSTEMS</span><span class="brand__dot"></span></h2>

  <header class="identity">
    <h1 class="identity__name">Matthias Lorbeer</h1>
    <p class="identity__role">WEB DEVELOPER</p>
  </header>

  <section class="contact">
    <p class="contact__company">Lorbeer Systems</p>
    <p class="contact__phone">+41 76 418 57 90</p>
    <p class="contact__email">matthias@lorbeer-systems.ch</p>
    <p class="contact__web">www.lorbeer-systems.ch</p>
  </section>
</main>
</body>
</html>
```